Natural Foods Start-up Needs a Snack Food Packaging Design

We are a natural foods company doing it differently. We don’t care about the need for consumers to make better food choices according to their enlightened self-interest. Let’s face it, their own health or the planet’s health often doesn’t REALLY matter to them. So it doesn’t drive us. The bottom line is that they want food that tastes damn good. It’s OUR job to make sure it is healthy and sustainable, all while tasting better than industrial alternatives.
We are launching a line of a carnivorous/high protein food. Think nutritious value of fish but tastes nothing like fish. Think snack, fast food, something that truck drivers would like (heard the 9-minute VIGOR story? Learn in!). Food that you eat with your fingers, and you lick your fingers when you are done, maybe tasting some of the motor oil that is left on your fingers from the oil change you did yourself on your KRV.
We are “Summit” because we want to be big but not grand. We are to the point, and use plain language. We use words like “Epic” and “Big” and “More” and “Sky”. Think Montana. Unfortunately, we are not very intuitive. But we don’t try too hard either, we don’t say we are “tough” or “hardy” or make any overwrought claims at all. We are a bit masculine, but the type of masculine energy that women don’t mind sometimes adopting themselves (of course we are not even a little sexist or asshole).
Package Design Guidelines
Package should be a clean, modern design that very simply tells you what is inside and why you should eat it. Should communicate good tasting food. Should also communicate “good for you” and “good for the planet” but these points should feel like afterthoughts.Remember, the customer buys this because it tastes good—later seeing that it is sustainable and healthy will only provide confirmation that they made the right choice (but NOT be the reason why they bought).
Name of product (for now) is “Summit FoodOrganic Snack Food” (please use these words as a placeholder). This should be prominently displayed on the package, using a large typeface. “Summit Food” can be larger than “Organic Snack Food”. Words like “Low in fat, high in protein, high in omega-3s, high in vitamins X, Y, Z and minerals A, B, C” should be displayed on the package front. Package should be the size/proportion of a small potato chip bag. Bag will be compostable plastic and will need a very large, prominent window to see product sealed inside.
Food comes in pieces and you can reach inside and pull one out and snack on it. It might compete with chips, beef jerky, nuts, or other such snacks. Should appeal to young buyers, probably mostly young professional men at first, but should also be accessible to women and children.

```html
<!DOCTYPE html>
<html lang="en">
<head>
<meta charset="utf-8">
<title>Summit Foods – Pack Back</title>
<link rel="stylesheet" href="https://fonts.googleapis.com/css2?family=PT+Sans&family=Roboto+Condensed:wght@400;700&family=Roboto+Slab:wght@400;700&display=swap">
<style>
  :root {
    --paper-light: #f4e6c4;
    --paper-mid: #e9d3a6;
    --paper-dark: #c9a871;
    --ink: #1d1a17;
    --sage: #7d9163;
    --brand-red: #b3212c;
    --white: #ffffff;
  }
  html, body { margin: 0; padding: 0; overflow: hidden; }
  .pack {
    position: relative;
    width: 801px; height: 1200px;
    overflow: hidden;
    color: var(--ink);
    font-family: "Roboto Condensed", "Arial Narrow", sans-serif;
  }
  .paper-texture {
    position: absolute; inset: 0;
    background: radial-gradient(ellipse 70% 55% at 50% 50%, var(--paper-light) 0%, var(--paper-mid) 60%, var(--paper-dark) 100%);
  }
  .cut-line {
    position: absolute; left: 0; right: 0; top: 89px;
    border-top: 1.5px dashed #3a332b;
  }
  .scissors { position: absolute; left: 58px; top: 79px; }

  .nutrition {
    position: absolute; left: 80px; top: 160px;
    width: 280px; height: 516px;
    border: 2px solid var(--ink);
    padding: 12px 12px 0 12px;
    font-family: "PT Sans", "Myriad Pro", sans-serif;
    font-size: 16px;
  }
  .nutrition h2 { margin: 0; font-weight: 400; font-size: 29px; line-height: 31px; }
  .nutrition .serving { line-height: 18px; }
  .bar-thick { border-top: 7px solid var(--ink); margin-top: 4px; }
  .bar-mid { border-top: 3px solid var(--ink); }
  .row {
    display: flex; justify-content: space-between;
    height: 26px; line-height: 27px;
    border-bottom: 1px solid var(--ink);
  }
  .row.indent { padding-left: 20px; }
  .row.plain { border-bottom: none; }
  .row.right { justify-content: flex-end; }
  .calories { text-decoration: line-through; }
  .footnote { font-size: 14px; line-height: 18px; padding-top: 6px; border-top: 3px solid var(--ink); padding-right: 6px; }

  .ingredients {
    position: absolute; left: 76px; top: 712px; width: 306px;
    font-size: 18.5px; line-height: 24px;
    hyphens: auto; -webkit-hyphens: auto;
  }
  .ingredients h3, .story h3 { margin: 0; font-weight: 400; font-size: 18.5px; }
  .ingredients p, .story p { margin: 0; }

  .contact {
    position: absolute; left: 66px; top: 881px;
    width: 327px; height: 74px;
    background: var(--sage);
    color: var(--white);
    text-align: center;
    white-space: nowrap;
    overflow: hidden;
    box-shadow: 0 3px 5px rgba(0,0,0,.25);
  }
  .contact strong {
    display: block; font-family: "Roboto Slab", serif; font-weight: 700; font-size: 24px;
    padding-top: 9px; line-height: 28px; letter-spacing: .5px;
  }
  .contact span { display: block; font-size: 21px; line-height: 28px; }

  .brand {
    position: absolute; left: 425px; top: 196px; width: 305px; text-align: center;
  }
  .brand-name {
    font-family: "Roboto Condensed", sans-serif; font-weight: 700;
    font-size: 45px; line-height: 46px; letter-spacing: 1px;
  }
  .brand-tag { font-size: 9px; letter-spacing: 1.5px; margin-top: 6px; }

  .story {
    position: absolute; left: 431px; top: 280px; width: 298px; height: 615px;
    overflow: hidden;
    font-size: 18.5px; line-height: 24.6px;
    hyphens: auto; -webkit-hyphens: auto;
  }

  .claim {
    position: absolute; left: 415px; top: 918px; width: 316px; text-align: center;
    font-family: "Roboto Slab", serif; font-weight: 700; color: var(--brand-red);
    font-size: 22px; line-height: 29px; letter-spacing: 1px;
  }

  .product-line {
    position: absolute; left: 0; width: 801px; top: 1078px; text-align: center;
    font-family: "PT Sans", sans-serif; font-size: 13.5px;
    transform: translateX(-10px);
  }
</style>
</head>
<body>
<div class="pack">
  <div class="paper-texture" role="img" aria-label="Aged parchment background with faint sunburst rays"></div>

  <div class="cut-line"></div>
  <svg class="scissors" width="32" height="20" viewBox="0 0 32 20" aria-hidden="true">
    <circle cx="6" cy="5" r="4" fill="none" stroke="#2a241e" stroke-width="2"/>
    <circle cx="6" cy="15" r="4" fill="none" stroke="#2a241e" stroke-width="2"/>
    <path d="M9 7 L30 15 M9 13 L30 5" stroke="#2a241e" stroke-width="2"/>
  </svg>

  <section class="nutrition">
    <h2>Nutrition Facts</h2>
    <div class="serving">Serving Size: 1 second spray (.5 ml)<br>Serving Per Container:354</div>
    <div class="bar-thick"></div>
    <div class="row">Amount Per Serving</div>
    <div class="row plain calories"><span>Calories: 4</span><span>Cal from Fat: 4</span></div>
    <div class="bar-mid"></div>
    <div class="row right">% Daily Value*</div>
    <div class="bar-mid" style="margin-top:6px"></div>
    <div class="row"><span>Total Fat Less than 1g</span><span>0%</span></div>
    <div class="row indent"><span>Saturated Fat 0g</span><span>0%</span></div>
    <div class="row indent"><span>Trans Fat 0g</span><span>0%</span></div>
    <div class="row indent"><span>Polyunsaturated Fat 0g</span></div>
    <div class="row indent"><span>Monounsaturated Fat 0g</span></div>
    <div class="row"><span>Cholesterol 0mg</span><span>0%</span></div>
    <div class="row"><span>Sodium 0mg</span><span>0%</span></div>
    <div class="row"><span>Total Carb 0g</span><span>0%</span></div>
    <div class="row plain"><span>Protein 0g</span><span>0%</span></div>
    <div class="footnote">Not a significant source of dietary fiber, sugar, vitamin A and C, calcium and iron.<br>*Percent Daily Values are based<br>on a 2000calorie diet.</div>
  </section>

  <section class="ingredients" lang="en">
    <h3>INGREDIENTS:</h3>
    <p>Lorem ipsum dolor sit amet, consectetur adipiscing elit. Etiam tempus turpis et mattis ultricies. Quisque convallis urna in eros vehicula interdum.</p>
  </section>

  <aside class="contact">
    <strong>Need more info:</strong>
    <span>email us at: info@summit.example</span>
  </aside>

  <header class="brand">
    <div class="brand-name">SUMMIT FOODS</div>
    <div class="brand-tag">GRASS FED JERKY</div>
  </header>

  <section class="story" lang="en">
    <h3>OUR STORY</h3>
    <p>&nbsp;Lorem ipsum dolor sit amet, consectetur adipiscing elit. Etiam tempus turpis et mattis ultricies. Quisque convallis urna in eros vehicula interdum. Ut sagittis justo eget dapibus pretium. Quisque non sem in elit dignissim vulputate sit amet in eros. Cras ante quam, vulputate ac feugiat ac, semper ut ligula. Aliquam ac volutpat est, ac sagittis risus. Etiam accumsan posuere lectus eget tincidunt. Donec non euismod justo, quis laoreet augue. Cras ac dolor quam. Duis imperdiet vulputate felis, nec dignissim elit semper nec. Donec sem felis, consectetur a molestie sit amet, viverra eu enim. Nullam eget posuere est. Etiam vel finibus arcu. Pellentesque interdum erat et ante finibus, quis molestie ligula cursus. Praesent ut elit in sem blandit condimentum vitae vitae orci. Aenean in tortor fermentum mi semper varius eu eget massa.vehicula, libero nibh posu</p>
  </section>

  <div class="claim">All Natural<br>ORGANIC SNACK FOOD</div>

  <div class="product-line">SUMMIT FOODS BEEF JERKY</div>
</div>
</body>
</html>
```